POP ART / Benny Coltrane type advertisment for medical practice

Our medical practice would like an ad resembling "Pop Art" / Benny Coltrane artwork.
We like outside-the-box advertisements and DO NOT want to look like a doctor's office / hospital / healthcare facility ad. It would be good to have an ad that can be used for full page and a modified one that could be used for quarter page ads that doesn't sacrifice the artistic vision you have created!
Reason: Would like more designs! Thanks!
Target Market(s)
adults 18-100+
Industry/Entity Type
Healthcare
Colors
Designer to choose colors to be used in the design.
Requirements
Must have
- must have photo of Dr. Talbrun
- his name Otto Talbrun, MD
- the practice logo
- the address: 41857 Pelican Drive, Suite 270, Mission Viejo, CA 92784
- phone: 949-555-0173
- website: www.fenwoodclinic.example
- tag line: Modern Medicine, Traditional Care
Nice to have
- family practice
- open daily
- book online
Should not have
- look like a doctor office or healthcare facility ad

```html
<!DOCTYPE html>
<html lang="en">
<head>
<meta charset="utf-8">
<title>Fenwood Medical Group – Modern Medicine, Traditional Care</title>
<link href="https://fonts.googleapis.com/css2?family=Dancing+Script:wght@600&family=Montserrat:wght@400;600;700&display=swap" rel="stylesheet">
<style>
  :root {
    --navy: #2b2f5e;
    --pink: #e5177b;
    --yellow: #fde52b;
    --blue: #3a74c9;
    --red: #e52a2f;
    --orange: #f39a3a;
    --white: #ffffff;
    --ink: #2b2f5e;
    --script: "Dancing Script", cursive;
    --sans: "Montserrat", Arial, sans-serif;
  }
  * { box-sizing: border-box; margin: 0; padding: 0; }
  html, body { width: 900px; height: 1200px; overflow: hidden; background: var(--white); }
  .ad { position: relative; width: 900px; height: 1200px; background: var(--white); }
  .tile { position: absolute; overflow: hidden; }
  .tile svg { position: absolute; }
  .portrait-top { left: 60px; top: 55px; width: 260px; height: 210px;
    background: linear-gradient(160deg, var(--blue) 0%, #5a8fe0 45%, var(--orange) 100%); }
  .modern { left: 320px; top: 55px; width: 260px; height: 210px; background: var(--navy); }
  .medicine { left: 580px; top: 55px; width: 260px; height: 210px; background: var(--pink); }
  .active { left: 60px; top: 265px; width: 260px; height: 215px; background: var(--pink); }
  .forms { left: 320px; top: 265px; width: 260px; height: 215px; background: var(--navy); }
  .heart { left: 580px; top: 265px; width: 260px; height: 215px; background: var(--yellow); }
  .care { left: 60px; top: 480px; width: 520px; height: 235px; background: var(--navy); color: var(--white); padding: 26px 34px; }
  .portrait-bottom { left: 580px; top: 480px; width: 260px; height: 235px;
    background: linear-gradient(200deg, #4a86dc 0%, var(--blue) 55%, #e8b27a 100%); }
  .script { font-family: var(--script); font-weight: 600; color: var(--white); line-height: 1; }
  .modern .script { position: absolute; top: 18px; left: 0; width: 100%; text-align: center; font-size: 46px; }
  .medicine .script { position: absolute; top: 18px; left: 0; width: 100%; text-align: center; font-size: 44px; }
  .figure-slot { position: absolute; left: 75px; top: 40px; width: 110px; height: 135px;
    background: var(--yellow); border-radius: 50% 50% 40% 40%; opacity: .9; }
  .care .script { font-size: 64px; margin-bottom: 26px; }
  .doctor-name { font-family: var(--sans); font-weight: 600; font-size: 30px; letter-spacing: .5px; margin-bottom: 8px; }
  .services { list-style: none; font-family: var(--sans); font-size: 19px; line-height: 1.35; }
  .services li::before { content: "• "; }
  .brand { position: absolute; left: 60px; top: 790px; display: flex; align-items: center; gap: 12px; }
  .brand-mark { width: 38px; height: 38px; background: var(--navy); }
  .brand-name { font-family: var(--sans); font-weight: 700; font-size: 30px; color: var(--navy); }
  .contact { position: absolute; left: 60px; top: 862px; font-family: var(--sans); font-size: 15px; color: var(--ink); line-height: 1.6; }
</style>
</head>
<body>
<main class="ad">
  <div class="tile portrait-top" role="img" aria-label="Pop art portrait photo of Dr. Otto Talbrun on a blue background"></div>

  <div class="tile modern">
    <p class="script">Modern</p>
    <svg width="260" height="210" viewBox="0 0 260 210" aria-hidden="true">
      <path d="M130 82c-34 0-58 20-58 46 0 14 7 26 19 34l-6 22 24-13c7 2 14 3 21 3 34 0 58-20 58-46s-24-46-58-46z" fill="none" stroke="var(--white)" stroke-width="5"/>
      <rect x="120" y="106" width="20" height="46" fill="var(--white)"/>
      <rect x="107" y="119" width="46" height="20" fill="var(--white)"/>
    </svg>
  </div>

  <div class="tile medicine">
    <p class="script">Medicine</p>
    <svg width="260" height="210" viewBox="0 0 260 210" aria-hidden="true">
      <g fill="none" stroke="var(--yellow)" stroke-width="6" stroke-linecap="round">
        <path d="M92 82v34c0 22 16 36 32 36s32-14 32-36V82"/>
        <path d="M124 152v14c0 16 14 24 30 24s28-10 28-26v-14"/>
        <circle cx="182" cy="140" r="12"/>
      </g>
      <circle cx="92" cy="80" r="5" fill="var(--yellow)"/>
      <circle cx="156" cy="80" r="5" fill="var(--yellow)"/>
    </svg>
  </div>

  <div class="tile active">
    <div class="figure-slot" role="img" aria-label="Yellow illustration of a person jumping for joy"></div>
  </div>

  <div class="tile forms">
    <svg width="260" height="215" viewBox="0 0 260 215" aria-hidden="true">
      <g fill="none" stroke="var(--white)" stroke-width="5" stroke-linejoin="round">
        <path d="M104 62h44l22 22v72h-66z"/>
        <path d="M148 62v22h22"/>
      </g>
      <path d="M120 124l12 12 22-26" fill="none" stroke="var(--white)" stroke-width="5" stroke-linecap="round" stroke-linejoin="round"/>
      <rect x="78" y="60" width="12" height="80" rx="3" fill="var(--pink)"/>
      <path d="M78 140h12l-6 14z" fill="var(--pink)"/>
    </svg>
  </div>

  <div class="tile heart">
    <svg width="260" height="215" viewBox="0 0 260 215" aria-hidden="true">
      <path d="M130 170l-48-46c-16-16-14-40 4-50 14-8 32-3 44 12 12-15 30-20 44-12 18 10 20 34 4 50z" fill="var(--red)"/>
      <g stroke="var(--white)" stroke-width="5" stroke-linecap="round">
        <line x1="130" y1="30" x2="130" y2="48"/>
        <line x1="72" y1="52" x2="84" y2="64"/>
        <line x1="188" y1="52" x2="176" y2="64"/>
        <line x1="52" y1="110" x2="68" y2="110"/>
        <line x1="208" y1="110" x2="192" y2="110"/>
      </g>
    </svg>
  </div>

  <section class="tile care">
    <h2 class="script">Traditional Care</h2>
    <h1 class="doctor-name">Otto Talbrun, MD</h1>
    <ul class="services">
      <li>family practice</li>
      <li>open daily</li>
      <li>book online</li>
    </ul>
  </section>

  <div class="tile portrait-bottom" role="img" aria-label="Pop art portrait photo of Dr. Otto Talbrun smiling, on a blue background"></div>

  <div class="brand">
    <span class="brand-mark"></span>
    <span class="brand-name">Fenwood Medical Group</span>
  </div>

  <address class="contact" style="font-style: normal;">
    41857 Pelican Drive, Suite 270, Mission Viejo, CA 92784<br>
    t: 949-555-0173 &nbsp; www.fenwoodclinic.example
  </address>
</main>
</body>
</html>
```